Occupational Therapist does home accessibility for disabled folks; needs business card design

We need a business card for a company in Portland, Oregon that specializes in making homes accessible, comfortable, and functional for people who are disabled or aging who would like to stay in THEIR home. Our medical background as Occupational Therapists allows us to translate the functional needs of the person into the recommendations for the design of the home remodel.

Target Market(s)

Elderly, children of elderly
People with disabilities, families of people with disabilities

Industry/Entity Type

Business

Contact Information for Business Card

Company name: HomeWise
Name: Danielle Reyes Crawford, OTR/L, CAPS, ECHM
Occupational Therapist, Home Modification & Accessibility Specialist
website: www.homewiseforyears.com
email: homewiseforyears@nestmail.example
phone: (503)218-4057
CCB #: 487315

Font styles to use
Sans Serif

Requirements
Must have
• My logo
• Easy to read font with contrasting background
• Please list the Services offered: Occupational Therapy, Home safety & accessibility assessments, Home modification consulting, project management
Nice to have
• Friendly, welcoming feel
Should not have
• Dark colored background

```html
<!DOCTYPE html>
<html lang="en">
<head>
<meta charset="utf-8">
<title>HomeWise Business Card</title>
<link rel="stylesheet" href="https://fonts.googleapis.com/css2?family=Lato:wght@400;700&display=swap">
<style>
  :root {
    --orange: #c97a27;
    --orange-light: #e8a230;
    --grey: #5f5f5f;
    --grey-dark: #4a4a4a;
    --paper: #fbfbfb;
    --backdrop: #e9e9e9;
    --line: #6a6a6a;
  }
  * { margin: 0; padding: 0; box-sizing: border-box; }
  html, body { width: 1200px; height: 900px; overflow: hidden; }
  body {
    background: var(--backdrop);
    font-family: 'Lato', sans-serif;
    color: var(--grey);
    position: relative;
  }
  .card {
    position: absolute;
    left: 250px;
    width: 700px;
    height: 400px;
    background: var(--paper);
    box-shadow: 0 2px 10px rgba(0,0,0,0.12);
    overflow: hidden;
  }
  .card--services { top: 30px; }
  .card--contact { top: 470px; }

  /* services side */
  .divider {
    position: absolute;
    left: 0; right: 0; top: 150px;
    height: 2px;
    background: var(--line);
  }
  .brand-ring {
    position: absolute;
    left: 100px; top: 55px;
    width: 190px; height: 190px;
    border: 7px solid var(--grey);
    border-radius: 50%;
    background: var(--paper);
    display: flex; align-items: center; justify-content: center;
  }
  .brand-name {
    font-weight: 700;
    color: var(--orange);
    font-size: 34px;
    letter-spacing: 0.5px;
  }
  .services {
    position: absolute;
    list-style: none;
    font-size: 21px;
    line-height: 1.3;
    color: var(--grey-dark);
  }
  .services li { position: relative; padding-left: 26px; margin-bottom: 4px; }
  .services li::before {
    content: "";
    position: absolute; left: 0; top: 9px;
    width: 10px; height: 10px;
    background: var(--orange);
  }
  .services--left { left: 60px; top: 275px; width: 360px; }
  .services--right { left: 340px; top: 170px; width: 340px; }
  .footer-band { position: absolute; left: 0; bottom: 0; width: 700px; height: 60px; }

  /* contact side */
  .brand-lockup {
    position: absolute;
    right: 60px; top: 60px;
    display: flex; align-items: center; gap: 14px;
  }
  .brand-lockup .mark {
    width: 30px; height: 30px;
    background: var(--orange);
  }
  .brand-lockup .brand-name { font-size: 52px; }
  .person {
    position: absolute;
    left: 60px; top: 205px;
  }
  .person-name { font-size: 30px; font-weight: 700; color: var(--orange-light); }
  .person-name .middle { color: var(--grey); }
  .credentials { font-size: 19px; margin-top: 2px; color: var(--grey-dark); }
  .contact-list {
    list-style: none;
    margin-top: 22px;
    font-size: 19px;
    color: var(--grey-dark);
  }
  .contact-list li { display: flex; align-items: center; gap: 12px; margin-bottom: 6px; }
  .contact-list svg { width: 18px; height: 18px; flex: none; }
  .licence {
    position: absolute;
    left: 455px; top: 205px;
    list-style: none;
    font-size: 19px;
    color: var(--grey-dark);
    line-height: 1.3;
  }
  .licence li { display: flex; gap: 12px; align-items: flex-start; }
  .licence svg { width: 16px; height: 16px; flex: none; margin-top: 4px; }
</style>
</head>
<body>

<section class="card card--services" aria-label="Card front: services">
  <div class="divider"></div>
  <div class="brand-ring"><span class="brand-name">HomeWise</span></div>
  <ul class="services services--right">
    <li>Home Modification Consulting</li>
    <li>Project Management</li>
  </ul>
  <ul class="services services--left">
    <li>Occupational Therapist</li>
    <li>Home Safety and Accessibility Assessments</li>
  </ul>
  <svg class="footer-band" viewBox="0 0 700 60" preserveAspectRatio="none" aria-hidden="true">
    <polygon points="0,38 700,38 700,60 0,60" fill="var(--orange)"/>
    <polygon points="560,38 600,0 700,0 700,38" fill="var(--grey)"/>
    <polygon points="0,38 560,38 600,0 600,38" fill="var(--orange)"/>
  </svg>
</section>

<section class="card card--contact" aria-label="Card back: contact details">
  <div class="brand-lockup">
    <span class="mark"></span>
    <span class="brand-name">HomeWise</span>
  </div>

  <div class="person">
    <p class="person-name">Danielle <span class="middle">Reyes</span> Crawford</p>
    <p class="credentials">OTR/L, CAPS, ECHM</p>
    <ul class="contact-list">
      <li>
        <svg viewBox="0 0 24 24" aria-hidden="true"><path fill="var(--orange)" d="M6.6 10.8a15 15 0 0 0 6.6 6.6l2.2-2.2c.3-.3.7-.4 1-.2 1.1.4 2.3.6 3.6.6.6 0 1 .4 1 1V20c0 .6-.4 1-1 1A17 17 0 0 1 3 4c0-.6.4-1 1-1h3.5c.6 0 1 .4 1 1 0 1.3.2 2.5.6 3.6.1.3 0 .7-.2 1z"/></svg>
        (503) 218-4057
      </li>
      <li>
        <svg viewBox="0 0 24 24" aria-hidden="true"><rect x="2" y="5" width="20" height="14" fill="var(--orange)"/><path d="M2 5l10 8 10-8" fill="none" stroke="var(--paper)" stroke-width="1.8"/></svg>
        homewiseforyears@nestmail.example
      </li>
      <li>
        <svg viewBox="0 0 24 24" aria-hidden="true"><g fill="none" stroke="var(--orange)" stroke-width="3" stroke-linecap="round"><path d="M10 14a4 4 0 0 0 5.7 0l3-3a4 4 0 0 0-5.7-5.7l-1 1"/><path d="M14 10a4 4 0 0 0-5.7 0l-3 3a4 4 0 0 0 5.7 5.7l1-1"/></g></svg>
        www.homewiseforyears.com
      </li>
    </ul>
  </div>

  <ul class="licence">
    <li>
      <svg viewBox="0 0 16 16" aria-hidden="true"><rect x="1" y="1" width="14" height="14" fill="var(--orange)"/></svg>
      CCB # : 487315
    </li>
    <li>
      <svg viewBox="0 0 24 24" aria-hidden="true"><path fill="var(--orange)" d="M12 2a7 7 0 0 0-7 7c0 5 7 13 7 13s7-8 7-13a7 7 0 0 0-7-7zm0 9.5A2.5 2.5 0 1 1 12 6.5a2.5 2.5 0 0 1 0 5z"/></svg>
      <span>5120 Fernhill Ct<br>Portland OR 97211</span>
    </li>
  </ul>
</section>

</body>
</html>
```